Business Card Design - cloud video monitoring

For the trade show in Las Vegas our company needs business cards with new brand - Vantrolux

The logo of the new brand is attached, the sample card with the founder's contact details is attached (just change the website to www.vantrolux.me) and email to info@vantrolux.me
Updates

                                        Forgot to say: the tagline for the brand is "the new normal cloud video management"

Industry/Entity Type

Business

```html
<!DOCTYPE html>
<html lang="en">
<head>
<meta charset="utf-8">
<title>Vantrolux Business Card</title>
<link href="https://fonts.googleapis.com/css2?family=Arimo:wght@400;700&family=Raleway:wght@200;400&display=swap" rel="stylesheet">
<style>
  :root {
    --stage: #2a1414;
    --card: #3c3c3e;
    --teal: #3fc4a3;
    --teal-soft: #7fb9aa;
    --teal-deep: #4f8f80;
    --ink-dark: #3a3f3e;
  }
  * { margin: 0; padding: 0; box-sizing: border-box; }
  html, body {
    width: 1200px;
    height: 800px;
    overflow: hidden;
    background: var(--stage);
  }
  .card {
    position: absolute;
    left: 75px;
    top: 100px;
    width: 1050px;
    height: 600px;
    background: var(--card);
    overflow: hidden;
  }
  .brand {
    position: absolute;
    left: 70px;
    top: 215px;
    display: flex;
    align-items: center;
    gap: 34px;
  }
  .brand-mark {
    flex: none;
    width: 130px;
    height: 130px;
    border-radius: 50%;
    background: var(--teal);
  }
  .brand-text {
    display: flex;
    flex-direction: column;
    gap: 6px;
  }
  .brand-name {
    font-family: "Raleway", sans-serif;
    font-weight: 400;
    font-size: 60px;
    line-height: 1;
    color: var(--teal);
    letter-spacing: 1px;
  }
  .brand-tagline {
    font-family: "Arimo", sans-serif;
    font-weight: 400;
    font-size: 15px;
    color: var(--teal);
    letter-spacing: 0.5px;
  }
  .contact {
    position: absolute;
    left: 590px;
    top: 78px;
    font-family: "Arimo", sans-serif;
    color: var(--teal);
    font-size: 20px;
    line-height: 1.25;
  }
  .contact-name { font-weight: 700; font-size: 23px; }
  .contact-role { margin-left: 22px; margin-bottom: 24px; }
  .contact-lines { margin-left: 46px; margin-bottom: 24px; }
  .contact-web { margin-left: 70px; }
  .contact-web p:last-child { margin-left: 20px; }
  .data-band {
    position: absolute;
    left: 0;
    top: 380px;
    width: 100%;
    height: 220px;
    background: linear-gradient(to bottom,
      rgba(63,196,163,0) 0%,
      rgba(90,150,138,0.35) 35%,
      var(--teal-deep) 62%,
      var(--teal-soft) 100%);
  }
  .site-url {
    position: absolute;
    left: 40px;
    bottom: 30px;
    font-family: "Raleway", sans-serif;
    font-weight: 200;
    font-size: 72px;
    color: var(--ink-dark);
    letter-spacing: 1px;
  }
</style>
</head>
<body>
  <main class="card">
    <div class="brand">
      <div class="brand-mark"></div>
      <div class="brand-text">
        <span class="brand-name">Vantrolux</span>
        <span class="brand-tagline">the new normal cloud video management</span>
      </div>
    </div>

    <section class="contact">
      <p class="contact-name">Mira Castellan</p>
      <p class="contact-role">Founder</p>
      <div class="contact-lines">
        <p>tel.: +1.555.204.7731</p>
        <p>fax: +1.555.318.4402</p>
      </div>
      <div class="contact-web">
        <p>info@vantrolux.me</p>
        <p>www.vantrolux.me</p>
      </div>
    </section>

    <div class="data-band" role="img" aria-label="Band of fading binary digits over a teal gradient"></div>
    <p class="site-url">www.vantrolux.me</p>
  </main>
</body>
</html>
```